Christmas Party Poster

I am promoting a Christmas Party for teenagers age 13-17 years old. The event is the first of its kind in our area, Weston Super Mare. The ticket price is to include food, soft drink's, music, entertainment.

There is nothing else of its kind in the the area or surrounding towns so a one of a kind event and new to the town. I would like the poster to be as simple and less busy as possible while still clearly showing the key information, anything that can be added it to show its a Christmas party for teenagers would be great. Also this is aimed at 13-17 year old's so as current and modern a design as possible.
Updates

A big thank you for the designs so far, As this is my first project I'm just getting the hang of what to ask for. I have slightly updated the brief and I now realize less is more, so long as the poster has the key elements of event name, date, time's, location, price and age range. The rest I should have been more flexible on. Thank you for your patience.

Target Market(s)

My Target Market are teenagers specifically 13-17 year olds

Industry/Entity Type

Town

Requirements
Must have
• The Title 'Frostlark' The venue is 'The Amber Pavilion w-s-m', Phone Number '01934 582093' Date '19th December'. Times '19.00 - 23.00'. Strictly u18 or age 13-17 years. Ticket price of £20. Chatterbox 'frost lark wsm' limited 4 tickets per person
Nice to have
• Christmas Party, Photo of your night out. Food and drink included
Should not have
• no worded reference to Santa, snowmen, reindeer, disco, try to keep out as not to offend cool teenagers.

```html
<!DOCTYPE html>
<html lang="en">
<head>
<meta charset="utf-8">
<title>Frostlark Christmas Party</title>
<link rel="stylesheet" href="https://fonts.googleapis.com/css2?family=Russo+One&family=Archivo+Black&family=Arimo:wght@700&display=swap">
<style>
  :root{
    --night:#050b1c;
    --deep:#0b1f46;
    --ice:#eef3fa;
    --steel:#6f86a6;
    --lime:#2ee86a;
    --white:#ffffff;
    --ball-blue:#3a58d8;
    --ball-pink:#c23ad8;
    --band:#03060f;
  }
  *{margin:0;padding:0;box-sizing:border-box}
  html,body{width:776px;height:1200px;overflow:hidden;background:var(--night)}
  .poster{
    position:relative;width:776px;height:1200px;overflow:hidden;
    font-family:"Arimo",Arial,sans-serif;font-weight:700;color:var(--white);
    background:radial-gradient(ellipse 700px 600px at 380px 400px, #0d1a38, var(--night) 90%);
  }
  .poster p{font-weight:700}
  .glitter-ball{
    position:absolute;left:124px;top:-162px;width:528px;height:528px;border-radius:50%;
    background:radial-gradient(circle at 35% 45%, #9fb6ff 0%, var(--ball-blue) 38%, var(--ball-pink) 80%, #5a1a80 100%);
  }
  .guides{position:absolute;inset:0}
  .lower-field{
    position:absolute;inset:0;
    clip-path:polygon(0 660px,776px 100px,776px 1200px,0 1200px);
    background:
      radial-gradient(ellipse 480px 380px at 300px 780px, rgba(80,130,200,.6), transparent 70%),
      linear-gradient(180deg, #0e2750 0%, #0b1f46 50%, #081632 100%);
  }
  .title{
    position:absolute;left:12px;top:405px;white-space:nowrap;
    font-family:"Russo One",sans-serif;font-size:124px;line-height:130px;letter-spacing:-3px;
    text-transform:uppercase;font-style:italic;
    transform:rotate(-18deg) scale(1,1.45);transform-origin:left center;
    background:linear-gradient(180deg,var(--ice) 0%,#c9d6e8 45%,var(--steel) 55%,#d9e3f1 100%);
    -webkit-background-clip:text;background-clip:text;color:transparent;
  }
  .subtitle{
    position:absolute;left:276px;top:506px;white-space:nowrap;
    font-family:"Russo One",sans-serif;font-size:50px;line-height:52px;text-transform:uppercase;
    transform:rotate(-16.5deg);transform-origin:left center;
    background:linear-gradient(180deg,var(--ice) 0%,#b7c6dc 50%,var(--steel) 100%);
    -webkit-background-clip:text;background-clip:text;color:transparent;
  }
  .when{position:absolute;right:28px;top:574px;text-align:right}
  .when .date{color:var(--lime);font-size:27px;line-height:32px}
  .when .time{font-size:20px;line-height:26px;margin-right:10px}
  .when .venue{font-size:16px;line-height:22px;margin-right:10px}
  .rule{position:absolute;left:216px;width:376px;height:2px;background:var(--white)}
  .rule.top{top:679px}.rule.bottom{top:760px}
  .ages{position:absolute;left:0;width:776px;top:697px;text-align:center;
    font-family:"Archivo Black",sans-serif;color:var(--lime);font-size:34px;line-height:44px}
  .highlights{position:absolute;left:26px;top:812px;width:740px;
    font-family:"Archivo Black",sans-serif;font-size:38px;line-height:48px;white-space:nowrap;
    transform:rotate(-2deg)}
  .highlights small{font-size:29px}
  .social{position:absolute;left:42px;top:946px;display:flex;align-items:center;gap:18px}
  .social .mark{width:60px;height:60px;background:var(--steel);border-radius:6px}
  .social p{font-size:14px;line-height:20px}
  .limit{position:absolute;left:520px;top:942px;width:200px;text-align:center;font-size:18px;line-height:26px}
  .price{position:absolute;left:0;width:808px;top:1042px;text-align:center;font-size:24px;line-height:36px}
  .phone-band{position:absolute;left:0;top:1146px;width:776px;height:54px;background:var(--band)}
  .phone{position:absolute;left:0;width:808px;top:1136px;text-align:center;color:var(--lime);
    font-size:36px;line-height:44px;letter-spacing:3px}
</style>
</head>
<body>
<main class="poster">
  <div class="glitter-ball" role="img" aria-label="Glittering mirrored party ball in blue and pink"></div>
  <div class="lower-field" role="img" aria-label="Deep blue night sky with soft light swirls and falling snow"></div>

  <svg class="guides" width="776" height="1200" viewBox="0 0 776 1200" aria-hidden="true">
    <line x1="0" y1="125" x2="776" y2="125" stroke="#fff" stroke-width="2" stroke-dasharray="10 8"/>
    <line x1="404" y1="0" x2="404" y2="1146" stroke="#fff" stroke-width="2" stroke-dasharray="10 8"/>
    <line x1="382" y1="230" x2="516" y2="1200" stroke="#2ee86a" stroke-width="2" stroke-dasharray="10 8"/>
    <line x1="372" y1="230" x2="500" y2="1200" stroke="#6fa6ff" stroke-width="1.5" stroke-dasharray="10 8"/>
    <polygon points="0,652 776,92 776,106 0,668" fill="#2ee86a"/>
  </svg>

  <h1 class="title">Frostlark</h1>
  <p class="subtitle">Christmas Party</p>

  <div class="when">
    <p class="date">19th December</p>
    <p class="time">19.00-23.00</p>
    <p class="venue">@ The Amber Pavilion, W-S-M</p>
  </div>

  <div class="rule top"></div>
  <p class="ages">Ages 13-17 years</p>
  <div class="rule bottom"></div>

  <p class="highlights"><small>The</small> Best Music, <small>and</small> Entertainment</p>

  <div class="social">
    <span class="mark"></span>
    <p>Find Us On<br>Chatterbox 'frost lark wsm'</p>
  </div>
  <p class="limit">Limited 4 Tickets<br>Per Person</p>

  <p class="price">Food And Drink Included<br>In Ticket Price Of £20</p>

  <div class="phone-band"></div>
  <p class="phone">01934 582093</p>
</main>
</body>
</html>
```